business card with logo

Would like a business card for an electrical contractor called BRANNOCK ELECTRICS.
No generic electrical imagery (light globe, powerpoints, ect). Would like a logo or symbol created in the design as part of the project . I would like crisp colour. No templated designs like Dorvex

is there any other designers willing to submit designs

Electrical

```html
<!DOCTYPE html>
<html lang="en">
<head>
<meta charset="utf-8">
<title>Brannock Electrics – Business Card</title>
<link rel="stylesheet" href="https://fonts.googleapis.com/css2?family=Montserrat:wght@300;400;700&display=swap">
<style>
  :root {
    --page-bg: #e6e6e4;
    --card-green: #cde3a0;
    --ink: #111111;
    --licence-white: #ffffff;
    --mark-green: #4e8a3a;
    --mark-fill: #ffffff;
  }
  * { margin: 0; padding: 0; box-sizing: border-box; }
  html, body {
    width: 1200px;
    height: 900px;
    overflow: hidden;
    background: var(--page-bg);
  }
  .canvas {
    position: relative;
    width: 1200px;
    height: 900px;
  }
  .business-card {
    position: absolute;
    left: 150px;
    top: 193px;
    width: 900px;
    height: 514px;
    border-radius: 28px;
    background: var(--card-green);
    box-shadow: 0 6px 18px rgba(0,0,0,0.15);
    font-family: "Montserrat", sans-serif;
    color: var(--ink);
    overflow: hidden;
  }
  .card-frame {
    position: absolute;
    inset: 0;
  }
  .licence-number {
    position: absolute;
    top: 12px;
    right: 56px;
    font-weight: 700;
    font-size: 20px;
    line-height: 24px;
    letter-spacing: 1px;
    color: var(--licence-white);
  }
  .company-name {
    position: absolute;
    top: 128px;
    left: 0;
    width: 100%;
    text-align: center;
    font-weight: 300;
    font-size: 58px;
    line-height: 70px;
    letter-spacing: 3px;
  }
  .brand-mark {
    position: absolute;
    left: 390px;
    top: 207px;
    width: 120px;
    height: 120px;
    border-radius: 50%;
    background: var(--mark-fill);
    border: 6px solid var(--mark-green);
    display: flex;
    align-items: center;
    justify-content: center;
  }
  .brand-mark-name {
    font-weight: 700;
    font-size: 15px;
    letter-spacing: 0.5px;
    color: var(--mark-green);
  }
  .contact-name {
    position: absolute;
    top: 334px;
    left: 0;
    width: 100%;
    text-align: center;
    font-weight: 400;
    font-size: 40px;
    line-height: 50px;
  }
  .contact-email {
    position: absolute;
    top: 392px;
    left: 0;
    width: 100%;
    text-align: center;
    font-weight: 400;
    font-size: 27px;
    line-height: 34px;
  }
</style>
</head>
<body>
<main class="canvas">
  <section class="business-card">
    <svg class="card-frame" width="900" height="514" viewBox="0 0 900 514" aria-hidden="true">
      <g fill="none" stroke="var(--ink)" stroke-width="1.5">
        <rect x="44" y="44" width="812" height="426" rx="6"/>
        <line x1="44" y1="267" x2="856" y2="267"/>
      </g>
    </svg>

    <p class="licence-number">REC#40318</p>
    <h1 class="company-name">BRANNOCK ELECTRICS</h1>
    <div class="brand-mark"><span class="brand-mark-name">BRANNOCK</span></div>
    <p class="contact-name">MARTIN KEALEY</p>
    <p class="contact-email">brannockelec@kestrelmail.com</p>
  </section>
</main>
</body>
</html>
```